Brivane - Business Cards for a new venture

create business card for a startup classified business dealing in construction materials, the cards need to have a professional look but modern, more serious than playful, one of the samples must include the official font (attached), please explore using the official colors in the company's logo

Target Market(s)

Energy sector

Contact Information for Business Card

Font styles to use
Other font styles liked:
• suissnord

Requirements
Must have
• corporate colors (in logo attached)
Nice to have
• Official font (in one of the samples) font is : suissnord
Should not have
• Cartoonish look

```html
<!DOCTYPE html>
<html lang="en">
<head>
<meta charset="utf-8">
<title>Brivane – Business Cards</title>
<link rel="stylesheet" href="https://fonts.googleapis.com/css2?family=Jost:wght@300;400&display=swap">
<style>
  :root {
    --navy: #042848;
    --brand-blue: #0a4473;
    --brand-blue-soft: #1d5688;
    --steel: #939598;
    --steel-soft: #a6a8ab;
    --white: #ffffff;
    --frame-light: #c9cacc;
    --frame-dark: #4a4b4d;
  }
  * { box-sizing: border-box; margin: 0; padding: 0; }
  html, body {
    width: 1200px; height: 1001px; overflow: hidden;
    background: var(--white);
    font-family: "Jost", "Futura", sans-serif;
  }
  .card {
    position: absolute;
    left: 197px; width: 830px;
    padding: 4px;
    background: linear-gradient(90deg, var(--frame-light), var(--frame-dark));
  }
  .card--front { top: 21px; height: 477px; }
  .card--back { top: 512px; height: 478px; }
  .card__face {
    position: relative; width: 100%; height: 100%; overflow: hidden;
  }
  .card--front .card__face { background: var(--white); }
  .card--back .card__face { background: var(--navy); }

  .edge-band {
    position: absolute; top: 82px; width: 30px; height: 275px;
  }
  .edge-band--left { left: 0; }
  .edge-band--right { right: 0; }
  .card--front .edge-band { background: linear-gradient(180deg, var(--brand-blue-soft), var(--brand-blue)); }
  .card--back .edge-band { background: linear-gradient(180deg, var(--steel-soft), var(--steel)); }

  .brand-mark { position: absolute; border-radius: 50%; }
  .card--front .brand-mark {
    width: 84px; height: 84px; left: 369px; top: 142px;
    background: var(--brand-blue);
  }
  .card--back .brand-mark {
    width: 52px; height: 52px; left: 385px; top: 362px;
    background: var(--steel);
  }
  .wordmark {
    position: absolute;
    color: var(--steel);
    font-weight: 400;
    text-transform: uppercase;
    white-space: nowrap;
    line-height: 1;
  }
  .card--front .wordmark {
    left: 0; right: 0; top: 313px; text-align: center;
    font-size: 42px; letter-spacing: 22px; padding-left: 22px;
  }
  .card--back .wordmark {
    right: 476px; top: 145px;
    font-size: 21px; letter-spacing: 9px; margin-right: -9px;
  }
  .card--back .wordmark { right: 467px; }
  .divider {
    position: absolute; left: 364px; top: 121px;
    width: 2px; height: 199px; background: var(--steel);
  }
  .contact {
    position: absolute; left: 376px; top: 130px;
    color: var(--white); font-weight: 300; font-size: 24px; line-height: 31px;
    list-style: none;
  }
  .contact__row { display: flex; white-space: nowrap; }
  .contact__label--name { width: 109px; }
  .contact__label--designation { width: 158px; }
  .contact__label--mobile { width: 149px; }
  .contact__label--office { width: 146px; }
  .contact__label--email { width: 140px; }
  .contact__label--address { width: 144px; }
</style>
</head>
<body>

<section class="card card--front" aria-label="Business card front">
  <div class="card__face">
    <div class="edge-band edge-band--left" role="img" aria-label="Blue decorative edge ornament"></div>
    <div class="edge-band edge-band--right" role="img" aria-label="Blue decorative edge ornament"></div>
    <span class="brand-mark" aria-hidden="true"></span>
    <h1 class="wordmark">Brivane</h1>
  </div>
</section>

<section class="card card--back" aria-label="Business card back">
  <div class="card__face">
    <div class="edge-band edge-band--left" role="img" aria-label="Grey decorative edge ornament"></div>
    <div class="edge-band edge-band--right" role="img" aria-label="Grey decorative edge ornament"></div>
    <h2 class="wordmark">Brivane</h2>
    <span class="divider" aria-hidden="true"></span>
    <ul class="contact">
      <li class="contact__row"><span class="contact__label--name">Name:</span><span>xxxxxxxx</span></li>
      <li class="contact__row"><span class="contact__label--designation">Designation:</span><span>xxxxxxxxxx</span></li>
      <li class="contact__row"><span class="contact__label--mobile">Mobile:</span><span>0123456789</span></li>
      <li class="contact__row"><span class="contact__label--office">Office:</span><span>0123456789</span></li>
      <li class="contact__row"><span class="contact__label--email">Email:</span><span>xxxxxxxxxmailbox.net</span></li>
      <li class="contact__row"><span class="contact__label--address">Address:</span><span>xxxxxxxxxxx</span></li>
    </ul>
    <span class="brand-mark" aria-hidden="true"></span>
  </div>
</section>

</body>
</html>
```